Falcrest security business card

Looking for a business card for my security company

Target Market(s)

Security

Industry/Entity Type

Security

Contact Information for Business Card

Name - Gil Marston. Title - General manager - direct 314 862.4490 website www. falcrestsecurityservices.example email - gil@ falcrestsecurityservices.example

Requirements
Must have
• Logo attached

```html
<!DOCTYPE html>
<html lang="en">
<head>
<meta charset="utf-8">
<title>Falcrest Security Services – Business Card</title>
<link rel="stylesheet" href="https://fonts.googleapis.com/css2?family=Exo+2:wght@500;600;700&display=swap">
<style>
  :root {
    --backdrop: #e4e8e9;
    --card: #000000;
    --gold: #c9a046;
    --gold-light: #f3dc98;
    --gold-deep: #8a6420;
    --band-text: #1a1408;
  }
  * { box-sizing: border-box; margin: 0; padding: 0; }
  html, body {
    width: 1200px;
    height: 900px;
    overflow: hidden;
    background: var(--backdrop);
    font-family: "Exo 2", Arial, sans-serif;
  }
  .sheet {
    width: 1200px;
    height: 900px;
    display: flex;
    flex-direction: column;
    align-items: center;
    justify-content: center;
    gap: 60px;
  }
  .card {
    position: relative;
    width: 640px;
    height: 366px;
    background: var(--card);
    color: var(--gold);
    overflow: hidden;
    box-shadow: 0 6px 18px rgba(0, 0, 0, 0.18);
  }

  /* Front */
  .card-front {
    display: flex;
    align-items: center;
    justify-content: center;
  }
  .brand {
    display: flex;
    align-items: center;
    gap: 18px;
  }
  .brand-mark {
    width: 22px;
    height: 22px;
    background: var(--gold);
  }
  .brand-name {
    font-weight: 700;
    font-size: 64px;
    letter-spacing: 3px;
    text-transform: uppercase;
    color: var(--gold);
    line-height: 1;
  }

  /* Back */
  .card-back .brand {
    position: absolute;
    left: 60px;
    top: 52px;
    gap: 12px;
  }
  .card-back .brand-mark { width: 14px; height: 14px; }
  .card-back .brand-name { font-size: 40px; letter-spacing: 2px; }

  .contact {
    position: absolute;
    left: 60px;
    top: 130px;
  }
  .contact-name {
    font-weight: 700;
    font-size: 26px;
    letter-spacing: 1px;
    text-transform: uppercase;
    line-height: 1;
  }
  .contact-title {
    font-weight: 600;
    font-size: 10px;
    letter-spacing: 3px;
    text-transform: uppercase;
    margin-top: 6px;
  }
  .contact-phone {
    font-weight: 700;
    font-size: 20px;
    letter-spacing: 1px;
    margin-top: 22px;
  }
  .contact-email {
    font-weight: 600;
    font-size: 17px;
    margin-top: 10px;
  }
  .web-band {
    position: absolute;
    left: 0;
    right: 0;
    bottom: 0;
    height: 48px;
    background: linear-gradient(90deg, var(--gold-deep) 0%, var(--gold-light) 45%, var(--gold) 70%, var(--gold-deep) 100%);
    display: flex;
    align-items: center;
    padding-left: 60px;
  }
  .web-address {
    font-weight: 700;
    font-size: 15px;
    letter-spacing: 2px;
    color: var(--band-text);
  }
</style>
</head>
<body>
  <main class="sheet">
    <section class="card card-front" aria-label="Card front">
      <div class="brand">
        <span class="brand-mark"></span>
        <span class="brand-name">Falcrest</span>
      </div>
    </section>

    <section class="card card-back" aria-label="Card back">
      <div class="brand">
        <span class="brand-mark"></span>
        <span class="brand-name">Falcrest</span>
      </div>
      <div class="contact">
        <p class="contact-name">Gil Marston</p>
        <p class="contact-title">General Manager</p>
        <p class="contact-phone">314 862.4490</p>
        <p class="contact-email">gil@falcrestsecurityservices.example</p>
      </div>
      <div class="web-band">
        <span class="web-address">www.falcrestsecurityservices.example</span>
      </div>
    </section>
  </main>
</body>
</html>
```